Sales Flyer Design for Cedarline Fryworks, Inc. this flyer should be bold, fun, attritive, and to the point

Our company is called Cedarline Fryworks, Inc. We collect used cooking for restaurants. We provide container for the customer to poor the frying oil into. We provide monthly rebates for cooking oil collected. We provide grease trap cleaning at charge for size of grease trap or grease interceptor. We need a flyer that is competitive and interesting to the potential customer. We would like it to be flashy and attractive. we would like a slot to leave a business card and a section to write a quote on the flyer. We want information about our company as well as the benefits of using our company. Please visit our website www.cedarlinefryworks.com to learn more about our company and what we do. We are family owned and operated. we have been in business since 1992. we service Oregon and Washington in the US. we provide the best service possible. we pick up quickly and are available for emergency calls.

Target Market(s)

Restaurants, retirement facilities, properties who manage several restaurants, sports arenas, schools, any business that has a kitchen or cooks food.

Industry/Entity Type

recycling of used cooking oils and grease trap materials

Font styles to use
Sans Serif

Colors
0054AA
0677BA
7BADD7
CADEEF
E8F1F8
0094D4
00A9DD
6FCCEA
C7EBF8
E9F6FB
59FF00
82FF00
B8FF75
E3FFCB
F4FFEA
FFF300
FFF600
FEFA6F
FFFEC7
FFFEE8
FFC000
F8CF3A
FAE287
FDF2CF
FEFAEE

Requirements
Must have
• a unique design that seperates uf from our competitors. an easy to understand and not to wordy flyer. we would like some animation such as an emoji with the money tongue hanging out when we mention rebating customers. we wants to express the hassle-free benefits of working with us. we want an emphasis on family owned since 1992
Nice to have
• cood color and balance, happy people shaking hands, images of clean oil collection containers, fancy looking vacuum trucks, overall, an engaging flyer that just doesn't get tossed in the dumpster without looking at it.
Should not have
• long paragraphs. Too much dialogue. No cliches. no boring photos.

```html
<!DOCTYPE html>
<html lang="en">
<head>
<meta charset="utf-8">
<title>Cedarline Fryworks, Inc. – Used Cooking Oil Recycling Flyer</title>
<link href="https://fonts.googleapis.com/css2?family=Montserrat:ital,wght@0,400;0,500;0,600;0,700;0,800;1,700&display=swap" rel="stylesheet">
<style>
  :root{
    --navy:#0054AA;
    --ocean:#0677BA;
    --sky:#0094D4;
    --mist:#CADEEF;
    --frost:#E8F1F8;
    --paper:#E9F6FB;
    --lime:#82FF00;
    --lime-soft:#E3FFCB;
    --gold:#FFC000;
    --lemon:#FFF300;
    --cream:#FFFEE8;
    --white:#ffffff;
    --ink:#0b2f57;
  }
  *{margin:0;padding:0;box-sizing:border-box}
  html,body{width:848px;height:1200px;overflow:hidden;background:var(--paper)}
  body{font-family:"Montserrat",sans-serif;color:var(--ink)}
  .flyer{position:relative;width:848px;height:1200px;overflow:hidden;background:var(--paper)}

  /* Hero */
  .hero{position:absolute;left:0;top:0;width:848px;height:465px;background:var(--navy);overflow:hidden}
  .hero-photo{position:absolute;left:470px;top:99px}
  .hero-chevrons{position:absolute;left:551px;top:0}
  .brand{position:absolute;left:33px;top:72px;color:var(--white);font-weight:800;font-size:45px;line-height:1.02;letter-spacing:.5px}
  .tagline{position:absolute;left:33px;top:228px;width:420px;color:var(--white);font-weight:600;font-size:25px;line-height:33px;text-transform:uppercase}
  .family-pill{position:absolute;left:33px;top:346px;padding:8px 18px;border-radius:22px;background:var(--gold);
    color:var(--navy);font-weight:800;font-size:18px;letter-spacing:.5px;text-transform:uppercase}

  .body-shapes{position:absolute;left:0;top:465px}

  /* Badges */
  .badge{position:absolute;width:258px;height:258px;border-radius:50%;
    box-shadow:0 6px 14px rgba(0,0,0,.3);text-align:center;text-transform:uppercase}
  .badge-title{display:inline-block;font-weight:800;font-size:33px;padding-bottom:4px;border-bottom:2px solid currentColor}
  .badge-sub{font-weight:700;font-size:15px;line-height:20px;margin-top:12px}
  .badge--services{left:32px;top:410px;padding-top:80px;background:var(--lime);color:var(--navy)}
  .badge--rebates{left:559px;top:662px;padding-top:76px;background:var(--gold);color:var(--navy);
    animation:wiggle 2.4s ease-in-out infinite}
  .badge--rebates .badge-sub{padding:0 34px}
  @keyframes wiggle{0%,100%{transform:rotate(0)}25%{transform:rotate(-4deg) scale(1.03)}75%{transform:rotate(4deg) scale(1.03)}}

  /* Copy */
  .intro{position:absolute;left:322px;top:500px;width:500px;font-size:17px;line-height:22px}
  .intro p+p{margin-top:16px}
  .intro em{font-style:italic;font-weight:700;color:var(--navy)}

  .steps{position:absolute;left:34px;top:745px;width:500px;font-size:17px;line-height:22px;list-style:none}
  .steps li+li{margin-top:14px}
  .steps b{font-style:italic;font-weight:700;color:var(--navy)}

  /* Quote + card slot */
  .quote-box{position:absolute;left:34px;top:922px;width:505px;height:118px;background:var(--white);
    border:2px solid var(--navy);border-radius:10px;padding:10px 16px}
  .quote-title{font-weight:800;font-size:15px;color:var(--navy);text-transform:uppercase;display:flex;justify-content:space-between}
  .quote-title span{font-weight:600;font-size:12px;text-transform:none;color:var(--ocean)}
  .quote-row{display:flex;align-items:flex-end;height:25px;font-size:14px;font-weight:600}
  .quote-row i{flex:1;margin-left:8px;border-bottom:1.5px solid var(--mist);height:18px}
  .card-slot{position:absolute;left:578px;top:932px;width:220px;height:108px;border:2px dashed var(--navy);
    border-radius:8px;background:var(--cream);display:flex;align-items:center;justify-content:center;
    text-align:center;font-weight:700;font-size:13px;line-height:17px;color:var(--navy);text-transform:uppercase}

  /* Footer */
  .contact-bar{position:absolute;left:0;top:1055px;width:848px;height:145px;background:var(--navy);color:var(--white)}
  .contact-chevrons{position:absolute;left:724px;top:-11px}
  .contact-item{position:absolute;top:27px;width:240px;text-align:center;font-size:18.5px;line-height:23px}
  .contact-item svg{display:block;margin:0 auto 12px}
  .contact-item--address{left:103px}
  .contact-item--phone{left:307px}
  .contact-item--hours{left:509px}
</style>
</head>
<body>
<div class="flyer">

  <header class="hero">
    <svg class="hero-photo" width="460" height="460" viewBox="0 0 460 460">
      <defs>
        <radialGradient id="oilPour" cx="55%" cy="45%" r="60%">
          <stop offset="0" stop-color="#ffffff"/>
          <stop offset=".45" stop-color="#FFFEE8"/>
          <stop offset=".75" stop-color="#F8CF3A"/>
          <stop offset="1" stop-color="#FFC000"/>
        </radialGradient>
      </defs>
      <circle cx="226" cy="226" r="206" fill="url(#oilPour)" role="img" aria-label="Fuel nozzle pouring golden recycled oil"/>
      <circle cx="226" cy="226" r="212" fill="none" stroke="var(--ocean)" stroke-width="14"/>
    </svg>
    <svg class="hero-chevrons" width="200" height="114" viewBox="0 0 200 114" aria-hidden="true">
      <polygon points="80,0 120,0 60,57 120,114 80,114 0,57" fill="var(--gold)"/>
      <polygon points="160,0 200,0 140,57 200,114 160,114 80,57" fill="var(--lemon)"/>
    </svg>
    <div class="brand">CEDARLINE<br>FRYWORKS, INC.</div>
    <h1 class="tagline">Oil recycling company in Oregon and Washington</h1>
    <div class="family-pill">Family owned since 1992</div>
  </header>

  <svg class="body-shapes" width="848" height="590" viewBox="0 0 848 590" aria-hidden="true">
    <polygon points="0,0 215,0 540,365 315,590 0,590" fill="var(--mist)"/>
    <polygon points="0,200 130,365 0,530" fill="var(--frost)"/>
  </svg>

  <div class="badge badge--services">
    <div class="badge-title">Services:</div>
    <div class="badge-sub">Used cooking oil<br>Grease trap cleaning</div>
  </div>

  <section class="intro">
    <p><em>At Cedarline Fryworks</em>, we collect used cooking oil and clean grease traps for any business with a kitchen: restaurants, schools, senior living, arenas, hotels and more.</p>
    <p><em>Hassle-free</em>: fast pickups, emergency calls welcome, and cash back every month.</p>
  </section>

  <ol class="steps">
    <li><b>Step 1:</b> We drop off free, clean containers for your fryer oil.</li>
    <li><b>Step 2:</b> We set a pickup schedule that fits your kitchen.</li>
    <li><b>Step 3:</b> Our techs vacuum your tank and log every gallon.</li>
    <li><b>Step 4:</b> You get a rebate check every single month.</li>
  </ol>

  <div class="badge badge--rebates">
    <div class="badge-title">Rebates</div>
    <div class="badge-sub">Get paid monthly for your used oil</div>
  </div>

  <section class="quote-box">
    <div class="quote-title">Your quote <span>www.cedarlinefryworks.com</span></div>
    <div class="quote-row">Oil per month:<i></i></div>
    <div class="quote-row">Grease trap size:<i></i></div>
    <div class="quote-row">Monthly rebate: $<i></i></div>
  </section>

  <div class="card-slot">Place business<br>card here</div>

  <footer class="contact-bar">
    <svg class="contact-chevrons" width="124" height="98" viewBox="0 0 124 98" aria-hidden="true">
      <polygon points="44,0 80,0 32,49 80,98 44,98 0,49" fill="var(--gold)"/>
      <polygon points="108,0 124,0 124,8 83,49 124,90 124,98 108,98 64,49" fill="var(--lemon)"/>
    </svg>
    <div class="contact-item contact-item--address">
      <svg width="30" height="40" viewBox="0 0 30 40" aria-hidden="true"><path d="M15 0C6.7 0 0 6.7 0 15c0 10 15 25 15 25s15-15 15-25C30 6.7 23.3 0 15 0zm0 21a6 6 0 1 1 0-12 6 6 0 0 1 0 12z" fill="var(--white)"/></svg>
      1840 NW Alder Ave.,<br>Portland, OR 97210
    </div>
    <div class="contact-item contact-item--phone">
      <svg width="26" height="42" viewBox="0 0 26 42" aria-hidden="true"><rect x="2" y="2" width="22" height="38" rx="3" fill="none" stroke="var(--white)" stroke-width="3"/><line x1="3" y1="32" x2="23" y2="32" stroke="var(--white)" stroke-width="2"/><circle cx="13" cy="36" r="1.6" fill="var(--white)"/></svg>
      503-555-0142<br>503-555-0187
    </div>
    <div class="contact-item contact-item--hours">
      <svg width="40" height="42" viewBox="0 0 40 42" aria-hidden="true"><rect x="2" y="6" width="36" height="34" rx="3" fill="none" stroke="var(--white)" stroke-width="3"/><rect x="2" y="6" width="36" height="8" fill="var(--white)"/><g fill="var(--white)"><rect x="9" y="1" width="3" height="9" rx="1.5"/><rect x="18.5" y="1" width="3" height="9" rx="1.5"/><rect x="28" y="1" width="3" height="9" rx="1.5"/><rect x="8" y="18" width="5" height="4"/><rect x="15" y="18" width="5" height="4"/><rect x="22" y="18" width="5" height="4"/><rect x="29" y="18" width="4" height="4"/><rect x="8" y="25" width="5" height="4"/><rect x="15" y="25" width="5" height="4"/><rect x="22" y="25" width="5" height="4"/><rect x="29" y="25" width="4" height="4"/><rect x="8" y="32" width="5" height="4"/><rect x="15" y="32" width="5" height="4"/></g></svg>
      Business Hours:<br>8:00 AM - 4:00 PM
    </div>
  </footer>

</div>
</body>
</html>
```